Mobile Optometry needs descriptive brochure and business cards for patients

I need a brochure design and business cards for a new optometry service that brings full ocular examination, refraction, and spectacle dispensing to the patient in need.
I will mainly be working out of senior homes so it needs to be very legible NO SMALL PRINT, CLEAR, CONSCIENCE.
The final design needs to incorporate the logo and colouring that was just selected from a previous project. I will add this file as soon as I get the final changes back from the designer.

Here is what I would like in the broacher. I don't have a fax number, website address, email address set up yet but have room for this.

Note: I have attached the logo I selected for the company. I may not have attached the most detailed version but this will give you an idea of colouring and style. I will upload the proper image soon.

Routine eye examinations are crucial for early detection of diseases of the eye and effects of systemic conditions for everybody. As we age we are at higher risk of vision loss due to Glaucoma, Age-related Macular Degeneration, Diabetic or Hypertensive Retinopathy, Cataracts and many other diseases.

During your complete ocular visual assessment you will be screened for all conditions that may be affecting you as well as treat any issues you may be suffering from. Common treatable complaints: Dry eyes, Watery eyes, Burning, Itching, Difficulty reading small print, Reduced distance vision, Glare, Light sensitiveness, and difficulty performing hobbies.

Here is what your complete examination includes

Step 1: Appointment Request
-Call
-Email
-Phone
-Fax

Step 2: Welcome form
-Patient Name, DOB, QR Wellcover number
-List current medications, allergies
-Current Visual difficulties
-Previous spectacle prescription (if available)

Step 3: Ocular Visual Assessment and Discussion of Results
-History & Symptoms
-Refraction
-Dilation and thorough ocular/retinal screening
-Spectacle or magnifier dispense if required
-Ophthalmologist or medical practitioner referral if required

Step 4: Dispense and Delivery
-Return to fit custom made glasses
-Demonstrate use low vision device
-Discuss any questions/treatments/referrals

I have just increased the budget. I am running out of time and want some good designs. I want a modern, clean and clear product. Please submit, points for originality.

Target Market(s)

The target audience is Professionals, managers, senior care facilities, families. I want something clean and easy to read. I want something modern but not trendy and something that appeals to the masses.

Industry/Entity Type

Medical

Font styles to use
Sans Serif

Requirements
Must have
• easy to read
bright
professional
Contact information on the last page
Nice to have
• order of services layer out nicely. Try a version with clearly defined steps. Step 1. Step 2. Step 3. Could be multiple broachers that are packaged together.
Should not have
• cartoony
serif fonts (please use font that is in logo)

```html
<!DOCTYPE html>
<html lang="en">
<head>
<meta charset="utf-8">
<title>Mobile Optometry – Complete Examination Brochure</title>
<link rel="stylesheet" href="https://fonts.googleapis.com/css2?family=Questrial&family=Didact+Gothic&display=swap">
<style>
  :root {
    --ink: #2b2b2b;
    --ink-soft: #4a4f55;
    --step-head: #a4b2ba;
    --step-band: #d6dbde;
    --step-body: #a9b6be;
    --step-white: #ffffff;
    --accent-teal: #8fb9c8;
    --divider: #e7f0f7;
    --panel-blue: #e6f0f8;
    --page: #ffffff;
  }
  * { box-sizing: border-box; margin: 0; padding: 0; }
  html, body { width: 1200px; height: 847px; overflow: hidden; background: var(--page); }
  .spread {
    position: relative; width: 1200px; height: 847px; overflow: hidden;
    font-family: "Questrial", "Century Gothic", sans-serif; color: var(--ink);
    background: var(--page);
  }
  .abs { position: absolute; }

  /* intro */
  .drop-cap {
    left: 52px; top: 14px; font-family: "Didact Gothic", sans-serif;
    font-size: 176px; line-height: 1; color: #111; font-weight: 400;
  }
  .intro {
    left: 168px; top: 36px; width: 420px; font-size: 16.6px; line-height: 34px; color: var(--ink);
  }
  .intro .tail { margin-left: -14px; }

  /* photos */
  .photo { border: 0; }
  .photo--exam-left {
    left: 0; top: 188px; width: 316px; height: 254px;
    background: linear-gradient(100deg, #c9d5dd 0%, #e8d6c8 40%, #dfe6ea 70%, #b8c6d0 100%);
  }
  .photo--exam-right {
    left: 332px; top: 188px; width: 246px; height: 254px;
    background: linear-gradient(110deg, #d9e2e8 0%, #c5d1d9 45%, #e7d9cc 75%, #cfd9df 100%);
  }
  .photo--eye-chart {
    left: 886px; top: 36px; width: 260px; height: 211px;
    background: linear-gradient(135deg, #f1f3f4 0%, #dfe3e6 55%, #c9b8a8 100%);
  }
  .photo--eye-closeup {
    left: 632px; top: 542px; width: 568px; height: 305px;
    background: radial-gradient(ellipse at 62% 48%, #7fb0c6 0%, #a9c6d3 16%, #e9d9cf 34%, #efe3da 60%, #f4ece6 100%);
  }

  .complaints {
    left: 178px; top: 216px; width: 288px; height: 288px; border-radius: 50%;
    background: rgba(255,255,255,0.78);
    box-shadow: 0 4px 18px rgba(0,0,0,0.12);
    text-align: center; color: var(--ink-soft);
    padding-top: 44px;
  }
  .complaints__title { font-size: 12.5px; line-height: 16px; letter-spacing: 0.5px; margin-bottom: 14px; }
  .complaints__list { list-style: none; font-size: 15px; line-height: 17px; }

  .section-title {
    left: 58px; top: 510px; font-size: 17px; letter-spacing: 1.4px; color: var(--accent-teal);
  }

  .divider { left: 592px; top: 36px; width: 18px; height: 774px; background: var(--divider); }
  .panel-blue { left: 886px; top: 247px; width: 314px; height: 263px; background: var(--panel-blue); }

  .assessment-note {
    left: 632px; top: 38px; width: 236px; font-size: 13.2px; line-height: 17px; color: #1f1f1f;
  }

  /* step cards */
  .step {
    border-radius: 11px; overflow: hidden; background: var(--step-body);
    box-shadow: 0 -3px 0 rgba(0,0,0,0.06) inset;
  }
  .step__head {
    background: var(--step-head); height: 72px; padding: 14px 0 0 16px;
    display: flex; align-items: flex-end; border-top: 3px solid #c2ccd2;
  }
  .step__word { font-size: 35px; line-height: 1; color: #1e1e1e; padding-bottom: 14px; }
  .step__num {
    font-size: 60px; line-height: 1; font-weight: 700; color: #f4f6f7;
    text-shadow: 2px 2px 3px rgba(0,0,0,0.25); margin-left: 4px; padding-bottom: 4px;
    font-family: "Didact Gothic", sans-serif;
  }
  .step__title {
    background: var(--step-band); color: #3b3f43; text-align: center;
    font-size: 17px; line-height: 17px; padding: 11px 8px;
  }
  .step__list {
    list-style: none; color: var(--step-white); font-weight: 700;
    font-size: 12.2px; line-height: 17px; padding: 12px 14px 10px 30px;
    font-family: "Didact Gothic", sans-serif;
  }
  .step__list li { position: relative; padding-left: 24px; }
  .step__list li::before { content: "•"; position: absolute; left: 0; }

  .step--1 { left: 54px; top: 544px; width: 246px; height: 254px; }
  .step--1 .step__list { padding-left: 72px; font-size: 13px; }
  .step--2 { left: 332px; top: 544px; width: 246px; height: 254px; }
  .step--3 { left: 632px; top: 170px; width: 236px; height: 342px; }
  .step--3 .step__title { padding: 12px 8px 14px; line-height: 17px; }
  .step--4 { left: 914px; top: 271px; width: 228px; height: 252px; }
  .step--4 .step__title { padding: 12px 8px 12px; }
</style>
</head>
<body>
<main class="spread">

  <div class="abs drop-cap" aria-hidden="true">A</div>
  <p class="abs intro">s we age we are at higher risk of vision loss due to Glaucoma, Age-related Macular Degeneration, Diabetic or Hypertensive Retinopathy, Cataracts and <span class="tail">many other diseases.</span></p>

  <div class="abs photo photo--exam-left" role="img" aria-label="Smiling patient looking into an eye examination instrument"></div>
  <div class="abs photo photo--exam-right" role="img" aria-label="Patient seated at a slit lamp during an eye examination"></div>

  <div class="abs complaints">
    <p class="complaints__title">COMMON<br>TREATABLE COMPLAINTS:</p>
    <ul class="complaints__list">
      <li>Dry Eyes</li>
      <li>Watery Eyes</li>
      <li>Burning</li>
      <li>Itching</li>
      <li>Difficulty reading small print</li>
      <li>Reduced distance vision</li>
      <li>Glare Light sensitiveness</li>
      <li>Difficulty performing</li>
      <li>hobbies</li>
    </ul>
  </div>

  <h2 class="abs section-title">HERE IS WHAT YOUR COMPLETE EXAMINATION INCLUDES...</h2>

  <section class="abs step step--1">
    <div class="step__head"><span class="step__word">Step</span><span class="step__num">1</span></div>
    <h3 class="step__title">Appointment Request</h3>
    <ul class="step__list">
      <li>Call</li><li>Email</li><li>Phone</li><li>Fax</li>
    </ul>
  </section>

  <section class="abs step step--2">
    <div class="step__head"><span class="step__word">Step</span><span class="step__num">2</span></div>
    <h3 class="step__title">Welcome Form</h3>
    <ul class="step__list">
      <li>Patient Name, DOB, QR Wellcover number</li>
      <li>List current medications, allergies</li>
      <li>Current Visual Difficulties</li>
      <li>Previous Spectacle prescription (if available)</li>
    </ul>
  </section>

  <div class="abs divider" aria-hidden="true"></div>

  <p class="abs assessment-note">During your complete ocular visual assessment you will be screened for all conditions that may be affecting you as well as treat any issues you may be suffering from.</p>

  <div class="abs photo photo--eye-chart" role="img" aria-label="Hand holding eyeglasses in front of an eye chart"></div>
  <div class="abs panel-blue" aria-hidden="true"></div>

  <section class="abs step step--3">
    <div class="step__head"><span class="step__word">Step</span><span class="step__num">3</span></div>
    <h3 class="step__title">Ocular Visual<br>Assessment and<br>Discussion<br>of Results</h3>
    <ul class="step__list">
      <li>History &amp; Symptoms</li>
      <li>Refraction</li>
      <li>Dilation and thorough ocular/retinal screening</li>
      <li>Spectacle or magnifier dispense if required</li>
      <li>Ophthalmologist or medical practitioner referral if required</li>
    </ul>
  </section>

  <section class="abs step step--4">
    <div class="step__head"><span class="step__word">Step</span><span class="step__num">4</span></div>
    <h3 class="step__title">Dispense and<br>Delivery</h3>
    <ul class="step__list">
      <li>Return to fit custom made glasses</li>
      <li>Demonstrate use low vision device</li>
      <li>Discuss any questions/ treatments/referrals</li>
    </ul>
  </section>

  <div class="abs photo photo--eye-closeup" role="img" aria-label="Close-up of a blue eye with long lashes"></div>

</main>
</body>
</html>
```